依頼詳細
比較する栄養素が多いので、どうすればお客様に見て頂きやすいか、
スマホで見た時に伝わりやすいかを重視したデザインにしていただきたいです。

添付している「参考画像」のようなグラフにしようと思ったのですが、
横長に作られており、スマホで見ると文字が小さくなって見づらいのではと思い
こちらでデザインを募らせていただく事となりました。

今のLPに差し込んでも違和感のないデザインでお願いします。

なお、今回はデザインのみでコーディングは必要ありません。
サイトURL
https://rinohaze.com/lp/
ページ数
1ページ
希望イメージ
シンプル 複雑
単色 カラフル
暗い 明るい
日常 高級
遊び心 厳粛
未来的 伝統的
女性的 男性的
希望する色
青系、無彩色系
納品ファイル
• 高解像度JPG (.jpg)
• イラストレーター形式 (.ai)
• フォトショップ形式 (.psd)
補足説明
■ 選んだ理由

一番バランスの良いデザインでした。

■ 提案者全員のお礼・コメント

この度は沢山のご提案ありがとうございました。
また機会がございましたら、どうぞよろしくお願いいたします。

```html
<!DOCTYPE html>
<html lang="ja">
<head>
<meta charset="utf-8">
<title>栄養素含有量 比較表</title>
<link href="https://fonts.googleapis.com/css2?family=Noto+Sans+JP:wght@400;500;700;900&display=swap" rel="stylesheet">
<style>
  :root {
    --navy: #1b2f6e;
    --gray-mid: #9a9a9a;
    --gray-light: #d2d2d2;
    --green: #3cae5a;
    --text: #1b2f6e;
    --bg: #ffffff;
  }
  * { margin: 0; padding: 0; box-sizing: border-box; }
  html, body { width: 744px; height: 1200px; overflow: hidden; background: var(--bg); }
  body { font-family: "Noto Sans JP", sans-serif; color: var(--text); position: relative; }

  .legend { position: absolute; left: 24px; top: 26px; }
  .legend-item { display: flex; align-items: center; gap: 8px; height: 24px; font-size: 9px; color: #555; }
  .legend-swatch { width: 56px; height: 9px; }
  .legend-swatch.ours { background: var(--navy); }
  .legend-swatch.common { background: var(--gray-mid); }
  .legend-swatch.other { background: var(--gray-light); }

  .title { position: absolute; left: 0; right: 0; top: 38px; text-align: center; font-size: 32px; font-weight: 900; letter-spacing: 2px; color: var(--navy); }

  .standard-pill { position: absolute; left: 150px; top: 172px; width: 124px; height: 30px; border-radius: 15px; background: var(--green); color: #fff; font-size: 15px; font-weight: 700; display: flex; align-items: center; justify-content: center; letter-spacing: 1px; }
  .standard-note { position: absolute; left: 290px; top: 172px; font-size: 8px; line-height: 1.4; color: var(--green); }
  .marker { position: absolute; top: 178px; width: 0; height: 0; border-left: 8px solid transparent; border-right: 8px solid transparent; border-top: 11px solid var(--green); }

  .guide { position: absolute; top: 208px; bottom: 40px; border-left: 2px dashed var(--green); opacity: .7; }

  .column { position: absolute; top: 210px; }
  .row { height: 72px; display: flex; align-items: center; }
  .label { font-size: 12px; font-weight: 500; text-align: center; line-height: 1.3; color: var(--navy); flex: none; white-space: nowrap; }
  .bars { position: relative; display: flex; flex-direction: column; gap: 4px; }
  .bar-main { display: flex; align-items: center; gap: 5px; }
  .bar.ours { background: var(--navy); height: 14px; }
  .bar.common { background: var(--gray-mid); height: 8px; }
  .bar.other { background: var(--gray-light); height: 8px; }
  .value { font-size: 11.5px; font-weight: 700; color: var(--navy); white-space: nowrap; }

  .col-a { left: 12px; } .col-a .label { width: 92px; } .col-a .bars { margin-left: 10px; }
  .col-b { left: 236px; } .col-b .label { width: 100px; } .col-b .bars { margin-left: 10px; }
  .col-c { left: 528px; } .col-c .label { width: 100px; } .col-c .bars { margin-left: 10px; }
</style>
</head>
<body>
  <div class="legend">
    <div class="legend-item"><span class="legend-swatch ours"></span>弊社サプリ 配合量</div>
    <div class="legend-item"><span class="legend-swatch common"></span>一般的なサプリ</div>
    <div class="legend-item"><span class="legend-swatch other"></span>他社製品 平均値</div>
  </div>

  <h1 class="title">栄養素含有量 比較表</h1>

  <div class="standard-pill">推奨基準値</div>
  <p class="standard-note">※厚生労働省の食事摂取基準<br>（成人1日あたり）</p>
  <span class="marker" style="left:422px"></span>
  <span class="marker" style="left:640px"></span>

  <div class="guide" style="left:213px"></div>
  <div class="guide" style="left:429px"></div>
  <div class="guide" style="left:647px"></div>

  <section class="column col-a">
    <div class="row"><div class="label">ビタミンA</div><div class="bars"><div class="bar-main"><span class="bar ours" style="width:40px"></span><span class="value">100 mcg</span></div><span class="bar common" style="width:18px"></span></div></div>
    <div class="row"><div class="label">β-カロテン</div><div class="bars"><div class="bar-main"><span class="bar ours" style="width:40px"></span><span class="value">2000 mcg</span></div><span class="bar other" style="width:34px"></span></div></div>
    <div class="row"><div class="label">ビタミンC</div><div class="bars"><div class="bar-main"><span class="bar ours" style="width:54px"></span><span class="value">200 mg</span></div><span class="bar common" style="width:42px"></span><span class="bar other" style="width:30px"></span></div></div>
    <div class="row"><div class="label">ビタミンD</div><div class="bars"><div class="bar-main"><span class="bar ours" style="width:14px"></span><span class="value">5.0 mcg</span></div><span class="bar common" style="width:10px"></span></div></div>
    <div class="row"><div class="label">ビタミンE</div><div class="bars"><div class="bar-main"><span class="bar ours" style="width:40px"></span><span class="value">50 mg</span></div><span class="bar common" style="width:12px"></span></div></div>
    <div class="row"><div class="label">ビタミンB1</div><div class="bars"><div class="bar-main"><span class="bar ours" style="width:40px"></span><span class="value">10 mg</span></div><span class="bar common" style="width:30px"></span><span class="bar other" style="width:24px"></span></div></div>
    <div class="row"><div class="label">ビタミンB2</div><div class="bars"><div class="bar-main"><span class="bar ours" style="width:40px"></span><span class="value">10 mg</span></div><span class="bar common" style="width:26px"></span><span class="bar other" style="width:22px"></span></div></div>
    <div class="row"><div class="label">ナイアシン</div><div class="bars"><div class="bar-main"><span class="bar ours" style="width:40px"></span><span class="value">20 mg</span></div><span class="bar common" style="width:30px"></span></div></div>
    <div class="row"><div class="label">パントテン酸</div><div class="bars"><div class="bar-main"><span class="bar ours" style="width:40px"></span><span class="value">15 mg</span></div><span class="bar common" style="width:32px"></span></div></div>
    <div class="row"><div class="label">ビタミンB6</div><div class="bars"><div class="bar-main"><span class="bar ours" style="width:40px"></span><span class="value">15 mg</span></div><span class="bar common" style="width:36px"></span><span class="bar other" style="width:26px"></span></div></div>
    <div class="row"><div class="label">ビタミンB12</div><div class="bars"><div class="bar-main"><span class="bar ours" style="width:40px"></span><span class="value">10 mcg</span></div><span class="bar common" style="width:24px"></span></div></div>
    <div class="row"><div class="label">葉酸</div><div class="bars"><div class="bar-main"><span class="bar ours" style="width:40px"></span><span class="value">200 mcg</span></div><span class="bar common" style="width:30px"></span></div></div>
    <div class="row"><div class="label">ビオチン</div><div class="bars"><div class="bar-main"><span class="bar ours" style="width:40px"></span><span class="value">50 mcg</span></div><span class="bar common" style="width:18px"></span></div></div>
  </section>

  <section class="column col-b">
    <div class="row"><div class="label">カルシウム</div><div class="bars"><div class="bar-main"><span class="bar ours" style="width:50px"></span><span class="value">150 mg</span></div><span class="bar common" style="width:66px"></span></div></div>
    <div class="row"><div class="label">マグネシウム</div><div class="bars"><div class="bar-main"><span class="bar ours" style="width:32px"></span><span class="value">80 mg</span></div><span class="bar common" style="width:48px"></span></div></div>
    <div class="row"><div class="label">亜鉛</div><div class="bars"><div class="bar-main"><span class="bar ours" style="width:50px"></span><span class="value">5 mg</span></div><span class="bar common" style="width:32px"></span></div></div>
    <div class="row"><div class="label">マンガン</div><div class="bars"><div class="bar-main"><span class="bar ours" style="width:16px"></span><span class="value">1 mg</span></div><span class="bar common" style="width:10px"></span></div></div>
    <div class="row"><div class="label">クロム</div><div class="bars"><div class="bar-main"><span class="bar ours" style="width:16px"></span><span class="value">4 mcg</span></div><span class="bar common" style="width:8px"></span></div></div>
    <div class="row"><div class="label">セレン</div><div class="bars"><div class="bar-main"><span class="bar ours" style="width:16px"></span><span class="value">10 mcg</span></div><span class="bar common" style="width:10px"></span></div></div>
    <div class="row"><div class="label">鉄</div><div class="bars"><div class="bar-main"><span class="bar ours" style="width:50px"></span><span class="value">1 mg</span></div></div></div>
    <div class="row"><div class="label">モリブデン</div><div class="bars"><div class="bar-main"><span class="bar ours" style="width:16px"></span><span class="value">4 mcg</span></div></div></div>
    <div class="row"><div class="label">イノシトール</div><div class="bars"><div class="bar-main"><span class="bar ours" style="width:50px"></span><span class="value">4 mg</span></div></div></div>
    <div class="row"><div class="label">コリン</div><div class="bars"><div class="bar-main"><span class="bar ours" style="width:50px"></span><span class="value">4 mg</span></div></div></div>
    <div class="row"><div class="label">レシチン</div><div class="bars"><div class="bar-main"><span class="bar ours" style="width:50px"></span><span class="value">30 mg</span></div></div></div>
    <div class="row"><div class="label">Lトリプトファン</div><div class="bars"><div class="bar-main"><span class="bar ours" style="width:76px"></span><span class="value">40 mg</span></div></div></div>
    <div class="row"><div class="label">Lメチオニン</div><div class="bars"><div class="bar-main"><span class="bar ours" style="width:50px"></span><span class="value">3 mg</span></div></div></div>
  </section>

  <section class="column col-c">
    <div class="row"><div class="label">ルテイン</div><div class="bars"><div class="bar-main"><span class="bar ours" style="width:18px"></span><span class="value">1 mg</span></div></div></div>
    <div class="row"><div class="label">リコペン</div><div class="bars"><div class="bar-main"><span class="bar ours" style="width:18px"></span><span class="value">1 mg</span></div></div></div>
    <div class="row"><div class="label">ゼアキサンチン</div><div class="bars"><div class="bar-main"><span class="bar ours" style="width:18px"></span><span class="value">1 mg</span></div></div></div>
    <div class="row"><div class="label">パイナップル<br>抽出物</div><div class="bars"><div class="bar-main"><span class="bar ours" style="width:32px"></span><span class="value">25 mg</span></div></div></div>
    <div class="row"><div class="label">ローズヒップ<br>抽出物</div><div class="bars"><div class="bar-main"><span class="bar ours" style="width:18px"></span><span class="value">3 mg</span></div></div></div>
    <div class="row"><div class="label">レモンバイオ<br>フラボノイド</div><div class="bars"><div class="bar-main"><span class="bar ours" style="width:18px"></span><span class="value">3 mg</span></div></div></div>
    <div class="row"><div class="label">ポリフェノール</div><div class="bars"><div class="bar-main"><span class="bar ours" style="width:18px"></span><span class="value">3 mg</span></div></div></div>
    <div class="row"><div class="label">ビタミンP</div><div class="bars"><div class="bar-main"><span class="bar ours" style="width:24px"></span><span class="value">10 mg</span></div></div></div>
    <div class="row"><div class="label">コエンザイムQ10</div><div class="bars"><div class="bar-main"><span class="bar ours" style="width:24px"></span><span class="value">10 mg</span></div></div></div>
    <div class="row"><div class="label">スピルリナ原末</div><div class="bars"><div class="bar-main"><span class="bar ours" style="width:20px"></span><span class="value">5 mg</span></div></div></div>
    <div class="row"><div class="label">パパイヤ<br>抽出物</div><div class="bars"><div class="bar-main"><span class="bar ours" style="width:32px"></span><span class="value">25 mg</span></div></div></div>
    <div class="row"><div class="label">緑茶抽出物</div><div class="bars"><div class="bar-main"><span class="bar ours" style="width:38px"></span><span class="value">80 mg</span></div></div></div>
  </section>
</body>
</html>
```